Letterhead PT. Bima Raya Lestari Developer

Alo , My Company need a letterhead design for PT. Bima Raya Lestari Developer Real Estate , i need your each other creative design letterhead for my PT.Bima Raya Lestari Developer Real Estate guys
input my data in letterhead :
Address : Komp. Ruko Taman Sari Blok F No. 27
No. Telp : 0778 512 3364 / 0812 4395 7716
Email : bimarayalestari@mailbox-example.com
Website : www.bimarayalestari-example.com

Target Market(s)

Buyer Property Real Estate & Investor

Industry/Entity Type

Real Estate Development

Font styles to use
Serif
Sans Serif

Requirements
Must have
• according to your creative each other guys as long i need
• Address : Komp. Ruko Taman Sari Blok F No. 27
• No. Telp : 0778 512 3364 / 0812 4395 7716
• Email : bimarayalestari@mailbox-example.com
• Website : www.bimarayalestari-example.com
Nice to have
Should not have
• don't want another colour except : white , dark blue n gold suit to our logo developer real estate

```html
<!DOCTYPE html>
<html lang="en">
<head>
<meta charset="utf-8">
<title>Letterhead – PT. Bima Raya Lestari Developer</title>
<link rel="stylesheet" href="https://fonts.googleapis.com/css2?family=Open+Sans:wght@300;400;600;700&display=swap">
<style>
  :root {
    --navy: #0d3862;
    --gold: #c8973f;
    --amber: #b46d26;
    --paper: #ffffff;
    --ink: #3a3a3a;
    --backdrop: #e6e6e6;
  }
  * { margin: 0; padding: 0; box-sizing: border-box; }
  html, body { width: 1200px; height: 1200px; overflow: hidden; background: var(--backdrop); }
  body { font-family: "Open Sans", sans-serif; color: var(--ink); }

  .letterhead {
    position: absolute; left: 211px; top: 50px;
    width: 778px; height: 1100px;
    background: var(--paper);
    overflow: hidden;
  }
  .frame { position: absolute; left: 0; top: 0; width: 778px; height: 1100px; }

  .brand {
    position: absolute; left: 48px; top: 62px;
    display: flex; align-items: center; gap: 10px;
  }
  .brand-square { width: 18px; height: 18px; background: var(--gold); }
  .brand-name {
    font-weight: 700; font-size: 17px; letter-spacing: .5px;
    color: var(--navy); line-height: 1.15; text-transform: uppercase;
  }

  .contact {
    position: absolute; right: 36px; top: 26px;
    list-style: none; font-size: 11px; color: #fff; line-height: 1.55;
  }
  .contact li { display: flex; align-items: center; gap: 7px; }
  .contact svg { width: 10px; height: 10px; fill: #fff; flex: none; }

  .letter-body {
    position: absolute; left: 70px; top: 220px; width: 640px;
    font-size: 15px; font-weight: 300; line-height: 1.62;
  }
  .salutation { font-weight: 400; margin-bottom: 14px; }
  .letter-body p + p { margin-top: 32px; }

  .sign-off { position: absolute; left: 70px; top: 750px; }
  .signature {
    width: 120px; height: 60px; margin-bottom: 8px;
    background: linear-gradient(135deg, #d8d8d8, #ececec);
  }
  .signer-name { font-size: 20px; font-weight: 400; color: #222; }
  .signer-role { font-size: 14px; font-weight: 300; color: #555; margin-top: 2px; }

  .address {
    position: absolute; left: 56px; bottom: 30px;
    font-size: 13px; color: #fff; line-height: 1.45;
  }
</style>
</head>
<body>
<main class="letterhead">
  <svg class="frame" viewBox="0 0 778 1100" aria-hidden="true">
    <rect x="0" y="0" width="778" height="10" fill="var(--navy)"/>
    <polygon points="470,10 778,10 778,100 520,100" fill="var(--amber)"/>
    <polygon points="400,100 520,100 470,60" fill="var(--gold)"/>
    <polygon points="300,1090 778,910 778,1100 300,1100" fill="var(--navy)"/>
    <polygon points="0,1010 400,1010 400,1100 0,1100" fill="var(--gold)"/>
    <polygon points="400,1010 470,1010 400,1050" fill="var(--amber)"/>
    <rect x="0" y="1090" width="778" height="10" fill="var(--navy)"/>
  </svg>

  <div class="brand">
    <span class="brand-square"></span>
    <span class="brand-name">PT. Bima Raya Lestari<br>Developer</span>
  </div>

  <ul class="contact">
    <li><svg viewBox="0 0 10 10"><path d="M2 0l2 2-1 1.5a6 6 0 003.5 3.5L8 6l2 2-1.5 2C4 10 0 6 0 1.5z"/></svg>0778 512 3364</li>
    <li><svg viewBox="0 0 10 10"><path d="M2 0l2 2-1 1.5a6 6 0 003.5 3.5L8 6l2 2-1.5 2C4 10 0 6 0 1.5z"/></svg>0812 4395 7716</li>
    <li><svg viewBox="0 0 10 10"><path d="M0 2h10v6H0zM0 2l5 3 5-3" /></svg>bimarayalestari@mailbox-example.com</li>
    <li><svg viewBox="0 0 10 10"><circle cx="5" cy="5" r="4.5" fill="none" stroke="#fff"/><path d="M0.5 5h9M5 .5v9" stroke="#fff"/></svg>www.bimarayalestari-example.com</li>
  </ul>

  <section class="letter-body">
    <p class="salutation">Dear Mr. Smith,</p>
    <p>Lorem ipsum dolor sit amet, consectetur adipiscing elit. Donec orci purus, luctus vitae dignissim eu, iaculis sed purus. Vivamus faucibus, ipsum nec aliquet viverra, leo mauris condimentum ligula, sit amet sagittis enim ligula quis arcu. Nam egestas tortor id nisi porttitor mattis. In tortor ante, ultricies in suscipit a, tempus non massa. Vivamus et auctor mi. Fusce vel massa nulla. Phasellus nec eros mauris, et scelerisque orci. Donec malesuada orci vitae nulla accumsan porta a id massa. Quisque accumsan iaculis magna sit amet fringilla. Maecenas consequat, magna eget tincidunt semper, odio nibh rutrum mi, id feugiat ante nisi eu risus. Vestibulum nunc orci, rhoncus a placerat in, ultricies in mi. Cras mattis varius eros, vel fringilla nisi suscipit eget.</p>
    <p>Quisque scelerisque sagittis nulla at porttitor. Mauris a justo et tellus interdum tristique. Sed id augue vitae urna euismod commodo aliquet a quam. Pellentesque arcu velit, cursus et malesuada ut, consequat et diam. Nullam erat sem, rhoncus id ullamcorper vitae, rhoncus et arcu. In ultricies ultricies nulla, ut rutrum nisi iaculis at. Donec eu magna a metus ornare faucibus. Fusce aliquet faucibus ultricies. Morbi semper, est id tincidunt gravida, sem arcu adipiscing lacus, ac bibendum nulla leo eu purus. Quisque nec diam sed risus consectetur accumsan quis nibh. Vestibulum id purus lorem.</p>
  </section>

  <div class="sign-off">
    <div class="signature" role="img" aria-label="Handwritten signature"></div>
    <div class="signer-name">John Doe</div>
    <div class="signer-role">Co-Founder &amp; CEO</div>
  </div>

  <address class="address" style="font-style:normal">Komp. Ruko Taman Sari<br>Blok F No. 27</address>
</main>
</body>
</html>
```